Real Estate Team Needs Business Cards

Double sided - Team Member on Front, Team Leader on Back (back side will contain more details).
Colors to use:
Red = R: 233 G: 1 B: 2
Grey = R: 89 G: 89 B: 89
Black= R: 0 B: 0 B: 0
** MAIN FOCUS ** ( separate border, color, design, etc. to really stand out - whatever you think draws the most attention ) on both sides for "Sell for 1%‡" and "Buy & receive up to a 1% rebate‡". Must have fine print **
**Please make both sides stand out and look unique / different
Business card to have round corners (standard size 3.5" x 2").:
Document Trim Size
89 x 51 mm
1050 x 600 pixels
Full Bleed Size
92 x 54 mm
1085 x 635 pixels
Basic example provided. Please redesign as you see best. In your design - Please use the same picture on both sides. Name, address, phone number, email, etc. will be provided to the selected design. QR code on back side only if there is room (not important)

```html
<!DOCTYPE html>
<html lang="en">
<head>
<meta charset="utf-8">
<title>Brightfield Realty – Business Cards</title>
<link rel="stylesheet" href="https://fonts.googleapis.com/css2?family=PT+Sans:ital,wght@0,400;0,700;1,400;1,700&display=swap">
<style>
  :root {
    --red: #e90102;
    --grey: #595959;
    --black: #000000;
    --ink: #161616;
    --white: #ffffff;
    --card: #f8f8f8;
    --page: #e6e3df;
    --photo-top: #e9ebee;
    --photo-bottom: #2b4a86;
  }
  * { margin: 0; padding: 0; box-sizing: border-box; }
  html, body { width: 900px; height: 1200px; overflow: hidden; }
  body {
    background: var(--page);
    font-family: "PT Sans", Arial, sans-serif;
    color: var(--ink);
    position: relative;
  }
  .card {
    position: absolute;
    left: 75px;
    width: 767px;
    height: 438px;
    background: var(--card);
    border-radius: 16px;
    overflow: hidden;
    box-shadow: 0 4px 14px rgba(0,0,0,.18);
  }
  .card--front { top: 133px; }
  .card--back { top: 629px; }
  .abs { position: absolute; }
  .center-text { text-align: center; }

  /* brand lockup */
  .brand { position: absolute; width: 420px; text-align: center; }
  .brand__name {
    display: flex; align-items: center; justify-content: center; gap: 12px;
    font-weight: 700; font-size: 36px; letter-spacing: .5px;
    color: var(--black); text-transform: uppercase; line-height: 1;
  }
  .brand__mark { width: 22px; height: 22px; background: var(--red); flex: none; }
  .brand__rule {
    display: flex; align-items: center; gap: 8px; margin-top: 10px;
    font-size: 11px; font-weight: 700; color: var(--grey); letter-spacing: .5px;
  }
  .brand__rule::before, .brand__rule::after {
    content: ""; flex: 1; height: 2px; background: var(--red);
  }

  /* headline promotion: the main focus on both sides */
  .offer {
    position: absolute; width: 420px; text-align: center;
    color: var(--red); font-style: italic; font-weight: 700;
    font-size: 24px; line-height: 28px;
  }

  /* front */
  .front__photo {
    left: 0; top: 0; width: 300px; height: 340px;
    background: linear-gradient(180deg, var(--photo-top) 0%, var(--photo-top) 55%, var(--photo-bottom) 100%);
  }
  .front__bands { left: 0; top: 0; }
  .front__name {
    left: 0; top: 362px; width: 330px; color: var(--white);
    font-weight: 700; font-size: 24px; letter-spacing: 2px; line-height: 1.1;
  }
  .front__role { font-size: 19px; letter-spacing: 1.5px; display: block; }
  .front__web {
    left: 340px; top: 379px; width: 380px; color: var(--white);
    font-weight: 700; font-size: 21px; letter-spacing: 1px;
  }
  .services {
    left: 315px; top: 270px; width: 420px;
    font-size: 22px; line-height: 28px; color: var(--black);
  }

  /* back */
  .back__portrait { left: 48px; top: 41px; }
  .back__nameplate {
    left: 41px; top: 332px; width: 281px; height: 41px;
    background: var(--red); color: var(--white);
    font-weight: 700; font-size: 26px; letter-spacing: 2px; line-height: 41px;
  }
  .back__position {
    left: 41px; top: 379px; width: 281px;
    font-weight: 700; font-size: 18px; color: var(--black);
  }
  .contact {
    left: 327px; top: 311px; width: 420px;
    font-weight: 700; font-size: 20px; line-height: 30px; letter-spacing: 1px; color: var(--black);
  }
</style>
</head>
<body>

<section class="card card--front">
  <div class="abs front__photo" role="img" aria-label="Portrait photo of the team member in a navy suit and light blue tie"></div>
  <svg class="abs front__bands" width="767" height="438" viewBox="0 0 767 438" aria-hidden="true">
    <polygon points="335,370 767,370 767,412 357,412" fill="var(--black)"/>
    <polygon points="0,340 318,340 370,438 0,438" fill="var(--red)"/>
  </svg>
  <p class="abs front__name center-text">MARCUS ELLERY<span class="front__role">OWNER</span></p>
  <p class="abs front__web center-text">WWW.BRIGHTFIELDREALTY.COM</p>

  <div class="brand" style="left:315px; top:118px;">
    <div class="brand__name"><span class="brand__mark"></span>Brightfield Realty</div>
    <div class="brand__rule">INC., BROKERAGE</div>
  </div>
  <p class="offer" style="left:315px; top:200px;">Sell for 1%*<br>Buy &amp; Receive up to a 1% rebate*</p>
  <p class="abs services center-text">Free Home Evaluation<br>Advanced Property Search<br>Free Local Sold Reports</p>
</section>

<section class="card card--back">
  <svg class="abs back__portrait" width="270" height="270" viewBox="0 0 270 270" role="img" aria-label="Circular portrait photo of the team leader in a navy suit">
    <defs>
      <linearGradient id="portraitTone" x1="0" y1="0" x2="0" y2="1">
        <stop offset="0" stop-color="var(--photo-top)"/>
        <stop offset=".6" stop-color="var(--photo-top)"/>
        <stop offset="1" stop-color="var(--photo-bottom)"/>
      </linearGradient>
    </defs>
    <circle cx="135" cy="135" r="128" fill="url(#portraitTone)" stroke="var(--red)" stroke-width="9"/>
  </svg>
  <p class="abs back__nameplate center-text">MARCUS ELLERY</p>
  <p class="abs back__position center-text">POSITION</p>

  <div class="brand" style="left:327px; top:116px;">
    <div class="brand__name"><span class="brand__mark"></span>Brightfield Realty</div>
    <div class="brand__rule">INC., BROKERAGE</div>
  </div>
  <p class="offer" style="left:327px; top:215px;">Sell for 1%*<br>Buy &amp; Receive up to a 1% rebate*</p>
  <p class="abs contact center-text">PH: 555 014 2276 | &nbsp;M: 555 014 227<br>CONTACT@BRIGHTFIELDREALTY.COM<br>WWW.BRIGHTFIELDREALTY.COM</p>
</section>

</body>
</html>
```